Process Flow Chart for Real Estate Agency

We need a visual flow chart of the process of selling a home for our Real Estate Agency. This visual will be provided to all new staff to explain the process and also to potential clients to explain how detailed the process is. It needs to show each step as detailed in the attached word doc and use icons and arrows to show the direction of flow.

Target Market(s)

Staff & Potential Clients

Industry/Entity Type

Real Estate

Font styles to use
Sans Serif

Colors

Designer to choose colors to be used in the design.

Requirements
Must have
• Easy to read, lots of icons, colour coded with Agent in one colour, Admin in another (some tasks are either/or so not sure what to colour those ones.)
Nice to have
• Include one of the two attached logos

```html
<!DOCTYPE html>
<html lang="en">
<head>
<meta charset="utf-8">
<title>Linden Hale – Selling Process Flow Chart</title>
<link rel="stylesheet" href="https://fonts.googleapis.com/css2?family=Open+Sans:wght@400;600;700&display=swap">
<style>
:root{
  --agent:#86e27f; --agent-line:#3ea43a;
  --shared:#caa0e6; --shared-line:#8a58b3;
  --admin:#fff35a; --admin-line:#d3bd00;
  --prep:#86dfe2; --prep-line:#36aab0;
  --auction:#f8a862; --auction-line:#d77a2c;
  --flow:#d42a2a; --loop:#3aa6df;
  --ink:#1e1e1e; --brand:#2f6f3a; --muted:#6b6b6b;
}
html,body{margin:0;padding:0;width:873px;height:1200px;overflow:hidden;background:#fff}
.chart{position:relative;width:800px;height:1100px;transform:scale(1.09125,1.0909);transform-origin:0 0;font-family:"Open Sans",Arial,sans-serif;color:var(--ink)}
.flow{position:absolute;inset:0;width:800px;height:1100px}
.step{position:absolute;box-sizing:border-box;display:flex;align-items:center;padding:0 4px;font-size:4.6px;line-height:1.15;font-weight:600;border:0.8px solid;border-radius:2px;box-shadow:0.6px 0.8px 0 rgba(0,0,0,.18)}
.agent{left:30px;width:210px;background:var(--agent);border-color:var(--agent-line)}
.shared{left:285px;width:230px;background:var(--shared);border-color:var(--shared-line)}
.admin{left:555px;width:230px;background:var(--admin);border-color:var(--admin-line)}
.prep{background:var(--prep);border-color:var(--prep-line);justify-content:center;text-align:center}
.auction{background:var(--auction);border-color:var(--auction-line)}
.step.intro{padding-left:16px}
.intro-icon{position:absolute;left:3px;top:50%;width:8px;height:8px;margin-top:-4px}
.role{position:absolute;width:64px;height:48px;border-radius:50%;border:2px solid #9fe0a6;background:radial-gradient(circle at 50% 40%,#e9f2ff 0 40%,#bfd6ea 70%)}
.role-agent{left:265px;top:4px}
.role-admin{left:448px;top:4px}
.brand{position:absolute;left:612px;top:12px;width:180px}
.brand-mark{position:absolute;left:0;top:6px;width:24px;height:24px;background:var(--brand)}
.brand-name{position:absolute;left:30px;top:6px;font-size:17px;font-weight:700;color:var(--brand);white-space:nowrap}
.brand-tag{position:absolute;left:30px;top:28px;font-size:7px;color:var(--muted);white-space:nowrap}
.if-label{position:absolute;left:640px;top:347px;font-size:5px;font-weight:700;line-height:1}
</style>
</head>
<body>
<div class="chart">

  <svg class="flow" viewBox="0 0 800 1100" aria-hidden="true">
    <defs>
      <marker id="head" viewBox="0 0 6 6" refX="5" refY="3" markerWidth="4" markerHeight="4" orient="auto"><path d="M0 0L6 3L0 6z" fill="#d42a2a"/></marker>
      <marker id="loophead" viewBox="0 0 6 6" refX="5" refY="3" markerWidth="5" markerHeight="5" orient="auto"><path d="M0 0L6 3L0 6z" fill="#3aa6df"/></marker>
    </defs>
    <g stroke="#d42a2a" stroke-width="0.7" fill="none" marker-end="url(#head)">
      <line x1="240" y1="94" x2="285" y2="84"/>
      <line x1="240" y1="94" x2="555" y2="106"/>
      <line x1="555" y1="108" x2="515" y2="121"/>
      <line x1="515" y1="137" x2="555" y2="150"/>
      <line x1="555" y1="168" x2="240" y2="178"/>
      <line x1="240" y1="193" x2="555" y2="200"/>
      <line x1="555" y1="202" x2="240" y2="210"/>
      <line x1="240" y1="225" x2="555" y2="227"/>
      <line x1="555" y1="362" x2="240" y2="381"/>
      <line x1="240" y1="381" x2="285" y2="377"/>
      <line x1="240" y1="383" x2="555" y2="395"/>
      <line x1="240" y1="414" x2="285" y2="424"/>
      <line x1="515" y1="424" x2="555" y2="430"/>
      <line x1="555" y1="432" x2="515" y2="445"/>
      <line x1="515" y1="490" x2="555" y2="498"/>
      <line x1="555" y1="498" x2="240" y2="507"/>
      <line x1="240" y1="507" x2="285" y2="518"/>
      <line x1="515" y1="518" x2="555" y2="522"/>
      <line x1="555" y1="576" x2="515" y2="563"/>
      <line x1="515" y1="563" x2="555" y2="594"/>
      <line x1="515" y1="603" x2="555" y2="605"/>
      <line x1="515" y1="618" x2="555" y2="632"/>
      <line x1="240" y1="790" x2="285" y2="782"/>
      <line x1="240" y1="806" x2="555" y2="815"/>
      <line x1="555" y1="815" x2="515" y2="826"/>
      <line x1="515" y1="826" x2="555" y2="831"/>
      <line x1="515" y1="843" x2="555" y2="849"/>
      <line x1="555" y1="875" x2="240" y2="887"/>
      <line x1="240" y1="887" x2="555" y2="885"/>
      <line x1="240" y1="889" x2="285" y2="901"/>
      <line x1="515" y1="901" x2="555" y2="907"/>
      <line x1="555" y1="923" x2="240" y2="937"/>
      <line x1="240" y1="937" x2="555" y2="935"/>
      <line x1="240" y1="939" x2="285" y2="947"/>
      <line x1="515" y1="947" x2="555" y2="953"/>
      <line x1="515" y1="963" x2="555" y2="960"/>
      <line x1="555" y1="973" x2="240" y2="992"/>
      <line x1="240" y1="992" x2="555" y2="993"/>
      <line x1="240" y1="994" x2="285" y2="1001"/>
      <line x1="240" y1="1011" x2="555" y2="1019"/>
      <line x1="555" y1="1019" x2="240" y2="1028"/>
      <line x1="240" y1="1044" x2="555" y2="1048"/>
      <line x1="555" y1="1050" x2="240" y2="1067"/>
      <line x1="240" y1="1067" x2="555" y2="1068"/>
    </g>
    <g stroke="#d42a2a" stroke-width="0.7" fill="none">
      <polyline points="337,637 337,639 110,639 110,643"/>
      <polyline points="337,639 708,639 708,643"/>
      <line x1="230" y1="639" x2="230" y2="643"/><line x1="348" y1="639" x2="348" y2="643"/>
      <line x1="470" y1="639" x2="470" y2="643"/><line x1="590" y1="639" x2="590" y2="643"/>
      <polyline points="400,682 400,684 114,684 114,687"/>
      <polyline points="400,684 714,684 714,687"/>
      <line x1="201" y1="684" x2="201" y2="687"/><line x1="286" y1="684" x2="286" y2="687"/>
      <line x1="507" y1="684" x2="507" y2="687"/><line x1="599" y1="684" x2="599" y2="687"/>
    </g>
    <g stroke="#3aa6df" stroke-width="2.2" fill="none" stroke-linecap="round" marker-end="url(#loophead)">
      <path d="M268 118 q-22 4 -18 14"/>
      <path d="M26 178 q-14 6 -4 14"/>
      <path d="M26 222 q-14 6 -4 14"/>
      <path d="M26 400 q-14 6 -4 14"/>
      <path d="M268 600 q-16 4 -10 12"/>
      <path d="M26 1026 q-14 6 -4 14"/>
    </g>
    <path d="M655 380 q-25 16 -60 4" stroke="#9be24f" stroke-width="3" fill="none" marker-end="url(#loophead)"/>
  </svg>

  <!-- Header -->
  <div class="role role-agent" role="img" aria-label="Agent avatar illustration"></div>
  <div class="role role-admin" role="img" aria-label="Admin avatar illustration"></div>
  <div class="brand">
    <span class="brand-mark"></span>
    <span class="brand-name">Linden Hale</span>
    <span class="brand-tag">Real Estate · Local homes, honest advice</span>
  </div>

  <!-- First contact -->
  <div class="step agent intro" style="top:14px;height:14px"><svg class="intro-icon" viewBox="0 0 8 8"><circle cx="4" cy="4" r="4" fill="#3aa6df"/><path d="M2.6 2h1l.4 1-.6.5a3 3 0 0 0 1.2 1.2l.5-.6 1 .4v1a4 4 0 0 1-3.5-3.5z" fill="#fff"/></svg>Agent calls potential client to arrange a time to meet and obtain details about the property</div>
  <div class="step agent intro" style="top:30px;height:10px"><svg class="intro-icon" viewBox="0 0 8 8"><circle cx="4" cy="4" r="4" fill="#3aa6df"/><circle cx="4" cy="3.2" r="1.3" fill="#fff"/><path d="M1.8 6.4a2.2 2 0 0 1 4.4 0z" fill="#fff"/></svg>Agent ensures all decision makers will be present at meeting</div>
  <div class="step agent intro" style="top:43px;height:10px"><svg class="intro-icon" viewBox="0 0 8 8"><circle cx="4" cy="4" r="4" fill="#e2412b"/><rect x="2.8" y="1.6" width="2.4" height="4.8" rx=".4" fill="#fff"/></svg>Agent adds vendors contact details on phone</div>
  <div class="step agent intro" style="top:56px;height:10px"><svg class="intro-icon" viewBox="0 0 8 8"><rect x="0.5" y="1" width="7" height="6.5" rx="1" fill="#3a7fdf"/><rect x="1.5" y="3" width="5" height="3.6" fill="#fff"/></svg>Agent adds appointment to personal calendar</div>
  <div class="step agent intro" style="top:69px;height:10px"><svg class="intro-icon" viewBox="0 0 8 8"><path d="M0.5 1.5h7v4.5h-4l-2 1.5v-1.5h-1z" fill="#f2b233"/></svg>Agent sends SMS to potential client to thank them for the opportunity</div>

  <!-- Pre-listing -->
  <div class="step shared" style="top:78px;height:10px">Agent/Admin orders kit from Ashford's</div>
  <div class="step agent" style="top:89px;height:10px">Agent completes a TMP to provide to Admin for Prelisting kit prep</div>
  <div class="step admin" style="top:100px;height:15px">Admin prepares pre-listing kit with questionnaire, sample brochure &amp; cover letter, property magazine, agent profile booklet</div>
  <div class="step shared" style="top:114px;height:15px">Admin/Agent delivers pre-listing kit (preferably within the hour) &amp; SMS potential vendor</div>
  <div class="step shared" style="top:131px;height:12px">Admin/Agent to research &amp; print comparable Sales reports</div>
  <div class="step admin" style="top:141px;height:19px">Admin prepares TMP with Marketing Costs Selection booklet, Service Offering Selection booklet, Sales Agency Agreement &amp; Benefits Form, ARE</div>
  <div class="step admin" style="top:163px;height:10px">Admin enters potential Vendor into CRM &amp; set "Appraisal" Track</div>

  <!-- Appraisal -->
  <div class="step agent" style="top:171px;height:14px">Agent confirms appraisal on the morning of the appointment with an SMS</div>
  <div class="step agent" style="top:188px;height:10px">Agent meets with potential Vendor and completes the appraisal</div>
  <div class="step admin" style="top:194px;height:13px">Admin prepares written appraisal report hand/deliver with coffee vouchers &amp;/or gift</div>
  <div class="step agent" style="top:205px;height:10px">Agent hand-delivers report with coffee voucher or Marlowe's chocolates</div>
  <div class="step agent" style="top:218px;height:15px">Agent receives confirmation from vendor to proceed with listing &amp; arranges signing of Residential Sales Agency Agreement</div>

  <!-- Listing admin -->
  <div class="step admin" style="top:222px;height:10px">Admin checks Residential Sales Agency &amp; enters as Listing into CRM</div>
  <div class="step admin" style="top:234px;height:10px">Admin completes the "New Listing Checklist" and prepares black folder</div>
  <div class="step admin" style="top:245px;height:12px">Admin checks for Vendor email addresses &amp; if required call or SMS client to obtain</div>
  <div class="step admin" style="top:259px;height:12px">Admin sets track (New Listing 1) as at date of signing Sales Agency &amp; removes Appraisal trail (if applicable)</div>
  <div class="step admin" style="top:272px;height:9px">Admin completes the marketing section of CRM</div>
  <div class="step admin" style="top:282px;height:12px">Admin confirms if Marketing has been paid upfront and prints/saves Tax Invoice</div>
  <div class="step admin" style="top:296px;height:9px">Admin creates Property Folder in Network</div>
  <div class="step admin" style="top:307px;height:9px">Admin scans &amp; files Residential Sales Agency in Network folder</div>
  <div class="step admin" style="top:318px;height:9px">Admin creates OFI Folder (including rental appraisal from PropData)</div>
  <div class="step admin" style="top:329px;height:12px">Admin email/post "Thank You For Listing" letter with copy of Sales Agency Agreement &amp; Seller's Guide &amp; Marketing Tax Invoice</div>
  <div class="step admin" style="top:343px;height:9px">Admin sends Form 1 Request Email through to Ashford Forms</div>

  <div class="if-label">If auction</div>
  <div class="step auction" style="left:555px;width:78px;top:357px;height:10px">Agent books auctioneer</div>
  <div class="step auction" style="left:665px;width:120px;top:356px;height:20px">Admin completes auction day checklist and auction day paperwork checklist</div>

  <!-- Keys & marketing -->
  <div class="step shared" style="top:372px;height:10px">Agent/Admin creates and delivers Just Listed letterbox drops</div>
  <div class="step agent" style="top:375px;height:14px">Agent to organise a time to have dropped off or office or collect keys if Vendor agrees</div>
  <div class="step admin" style="top:390px;height:10px">Admin secures keys and stores in key safe</div>
  <div class="step agent" style="top:397px;height:10px">Agent organises Home Stylist, Floor Plan &amp; Photography</div>
  <div class="step agent" style="top:410px;height:10px">Agent adds appointments to personal calendar</div>
  <div class="step shared" style="top:419px;height:10px">Agent/Admin attends photography appointment at property</div>
  <div class="step admin" style="top:425px;height:12px">Admin receives proof photos and saves to Network Folder under "Proofs"</div>
  <div class="step shared" style="top:440px;height:10px">Agent/Admin selects photos for retouching</div>
  <div class="step shared" style="top:452px;height:9px">Agent/Admin emails photos to vendor for approval</div>
  <div class="step shared" style="top:463px;height:9px">Agent/Admin emails approved photo list to Linwood Print</div>
  <div class="step shared" style="top:474px;height:9px">Agent/Admin emails floor plan to vendor for approval</div>
  <div class="step shared" style="top:485px;height:9px">Agent/Admin completes write-up text and emails to vendor for approval</div>
  <div class="step admin" style="top:493px;height:10px">Admin uploads property onto internet on MONDAY</div>
  <div class="step agent" style="top:500px;height:14px">Agent confirms open time with Vendor &amp;/or Tenant and has Admin update online</div>
  <div class="step shared" style="top:512px;height:13px">Agent/Admin checks for newspaper advert request/budget in Sales Agency Agreement</div>
  <div class="step admin" style="top:517px;height:10px">Admin to place newspaper advert if requested</div>
  <div class="step admin" style="top:530px;height:10px">Admin orders signboard &amp; emails to vendor for approval</div>
  <div class="step admin" style="top:543px;height:10px">Admin to email vendor approval to Carter Bros</div>
  <div class="step admin" style="top:555px;height:12px">Admin to send write-up text &amp; floor plan to Linwood Print to create brochures</div>
  <div class="step shared" style="top:557px;height:12px">Agent/Admin to proof check brochures &amp; send approval to Linwood Print</div>
  <div class="step admin" style="top:570px;height:12px">Admin receives print ready brochure file from Linwood Print &amp; print inhouse</div>
  <div class="step admin" style="top:588px;height:9px">Admin to create &amp; display window card</div>
  <div class="step shared" style="top:597px;height:10px">Agent/Admin to create &amp; deliver First Open Invitation letterbox drop</div>
  <div class="step admin" style="top:600px;height:10px">Admin to submit editorial to Herald &amp; Courier</div>
  <div class="step shared" style="top:613px;height:10px">Agent/Admin adds property to Weekly Property Magazine</div>
  <div class="step shared" style="top:627px;height:10px;width:105px">Agent/Admin prepares for OFI:</div>
  <div class="step admin" style="top:627px;height:10px">Admin adds property to Weekly Property Magazine</div>

  <!-- OFI preparation -->
  <div class="step prep" style="left:60px;width:104px;top:643px;height:25px">For all new properties, secure the Agent's magnet with a paperclip onto the front cover of at least 30 brochures</div>
  <div class="step prep" style="left:180px;width:100px;top:643px;height:25px">Put brochures into a plastic folder and label using the label inside the cover of the black OFI folder</div>
  <div class="step prep" style="left:298px;width:100px;top:643px;height:25px">Put a brochure inside the plastic sleeve cover of the black OFI folder for new properties</div>
  <div class="step prep" style="left:420px;width:100px;top:643px;height:25px">Check other properties open over the weekend and ensure they have at least 20 brochures prepared with magnets secured</div>
  <div class="step prep" style="left:540px;width:100px;top:643px;height:25px">Check the black OFI folders are complete with rental assessments, offer forms and Form 1</div>
  <div class="step prep" style="left:658px;width:100px;top:643px;height:25px">Put the coloured plastic file box and the black OFI folder into a box with labels facing upwards</div>

  <div class="step shared" style="top:672px;height:10px;justify-content:center">Agent/Admin prepares the OFI basket with:</div>
  <div class="step prep" style="left:60px;width:108px;top:687px;height:17px">Current weekly magazines 2-3 per property to be opened</div>
  <div class="step prep" style="left:177px;width:48px;top:687px;height:10px">Full lolly jar</div>
  <div class="step prep" style="left:237px;width:98px;top:687px;height:10px">Wireless speaker with charger</div>
  <div class="step prep" style="left:358px;width:84px;top:687px;height:14px">Business card holder (with business cards)</div>
  <div class="step prep" style="left:470px;width:75px;top:687px;height:10px">Orange folder with Form R3's</div>
  <div class="step prep" style="left:558px;width:82px;top:687px;height:10px">At least 2 Little Helper's bags</div>
  <div class="step prep" style="left:668px;width:92px;top:687px;height:17px">Clipboard with OFI sheets &amp; extra offer forms and/or charged tablet</div>

  <!-- Open inspection -->
  <div class="step shared" style="top:720px;height:12px">Agent/Admin conducts OFI with standard HP setup - e.g., Music, lollies, etc</div>
  <div class="step shared" style="top:735px;height:10px">Agent/Admin records names and numbers of all attendees</div>
  <div class="step shared" style="top:749px;height:9px">Agent calls Vendor after OFI to update them</div>
  <div class="step shared" style="top:760px;height:12px">Agent/Admin generates thank you for attending text message to all attendees at conclusion of ofi</div>
  <div class="step shared" style="top:775px;height:14px">Agent/Admin completes call backs on Monday at the latest to organise 2nd viewings, obtain feedback and handle offers</div>

  <!-- Offers & contract -->
  <div class="step agent" style="top:785px;height:10px">Agent negotiates offers where applicable &amp; presents to Vendor</div>
  <div class="step agent" style="top:800px;height:13px">Agent to get written offer with all conditions &amp; copy of purchasers ID &amp; provide all paperwork to Admin</div>
  <div class="step admin" style="top:810px;height:10px">Admin types up contract</div>
  <div class="step shared" style="top:820px;height:12px">Agent/Admin gets contract signed by all parties along with acknowledgement of Form 1 documentation</div>
  <div class="step admin" style="top:825px;height:12px">Admin sends copy of Contract &amp; Form 1 with "Congratulations" Letter &amp; Moving Checklist to VENDOR &amp; PURCHASER</div>
  <div class="step shared" style="top:836px;height:14px">Agent/Admin places file with completed contract and Form 1 in the "Awaiting Deposit" tray for processing</div>
  <div class="step admin" style="top:844px;height:10px">Admin enters Purchaser details into CRM</div>
  <div class="step admin" style="top:857px;height:10px">Admin completes Sales Commission screen in CRM</div>
  <div class="step admin" style="top:870px;height:10px">Admin sets Settlement Trails for Purchaser and Vendor in CRM</div>
  <div class="step agent" style="top:882px;height:10px">Agent coordinates building &amp;/or pest inspections if required</div>
  <div class="step admin" style="top:880px;height:12px">Admin places reminder in calendar to follow up finance approval 2 days prior to due date, if required</div>
  <div class="step shared" style="top:896px;height:10px">Agent/Admin to attend building &amp;/or pest inspection</div>
  <div class="step admin" style="top:901px;height:12px">Admin completes Settlements spreadsheet including Under Contract tab in Network</div>
  <div class="step admin" style="top:917px;height:10px">Admin receipts deposit paid by purchaser</div>
  <div class="step agent" style="top:932px;height:10px">Agent updates property as UNDER CONTRACT on signboard</div>
  <div class="step admin" style="top:930px;height:10px">Admin updates property as UNDER CONTRACT online</div>
  <div class="step shared" style="top:942px;height:10px">Agent/Admin obtains Conveyancer details from Vendor &amp; Purchaser</div>
  <div class="step admin" style="top:946px;height:10px">Admin checks if Vendor Paid Marketing has been received</div>
  <div class="step shared" style="top:958px;height:10px">Agent/Admin to follow up finance approval (if applicable)</div>
  <div class="step admin" style="top:956px;height:11px">Admin completes cover sheet and sends with Contract and Form 1's to Conveyancers</div>
  <div class="step admin" style="top:968px;height:11px">Admin organises signboard removal for the day after settlement once contract is unconditional</div>

  <!-- Sold & settlement -->
  <div class="step agent" style="top:985px;height:14px">Agent updates property as sold on signboard &amp; get photo with Vendor &amp;/or Purchaser</div>
  <div class="step admin" style="top:988px;height:10px">Admin to print &amp; organise delivery of Just Sold campaign</div>
  <div class="step shared" style="top:996px;height:10px">Agent/Admin to post SOLD photos on Social Media</div>
  <div class="step agent" style="top:1005px;height:12px">Agent arranges with vendor to provide keys &amp; remove prior to settlement</div>
  <div class="step admin" style="top:1014px;height:10px">Admin prepares settlement gifts for both Vendor and Purchaser</div>
  <div class="step agent" style="top:1022px;height:13px">Agent calls purchaser to congratulate them and organise pick up or delivery of keys and gift</div>
  <div class="step agent" style="top:1038px;height:13px">Agent calls Vendor to congratulate them and organise to deliver gift and thank them once again</div>
  <div class="step admin" style="top:1043px;height:12px">Admin updates addresses, send service survey letters, set Anniversary tracks</div>
  <div class="step agent" style="top:1060px;height:15px">Agent calls Vendor &amp; Purchaser after settlement - 1 week, 1 month, 6 months</div>
  <div class="step admin" style="top:1062px;height:12px">Admin updates as SOLD online (display price unless otherwise instructed)</div>
  <div class="step admin" style="top:1077px;height:9px">Admin prepare file for archiving</div>
  <div class="step shared" style="left:235px;width:310px;top:1083px;height:11px;justify-content:center">Agent makes annual anniversary phone call and Admin sends card &amp; gift to Vendor &amp; Purchaser</div>

</div>
</body>
</html>
```